Business is called "Pelton Ledger". Accounting and tax services.

I need a flyer for my new business "Pelton Ledger". I am an individual accountant working for himself on the Sunshine Coast in Queensland Australia. I would like to see designs that communicate reliability and trust. I believe my point of difference is that I am always available to my clients and I will cap my number of clients to ensure I can service them properly. Accountants in general seem to have a bad reputation for not responding to clients in a timely fashion, whether by email or phone. This is where I intend to differentiate myself. I have included my business card for ideas on colour and for contact information. I have also included some logo's that should go on the flyer. With the QLA logo, the words "Pelton Ledger is a QLA Business" needs to be written either above, below or to the right hand side (as per the business card).

Target Market(s)

Small business owners and individuals requiring taxation and financials

Industry/Entity Type

Public Accounting

Font styles to use
Serif

Requirements
Must have
• Supplied logo's, accounting style pictures etc
Services: Small Business Taxation
Company & Trust Tax Returns
Rental Property Returns
Capital Gains Tax
Individual Tax Returns
BAS and IAS lodgements
Nice to have
• Needs to convey a sense of being reliable and responds to clients quickly.
Should not have
• My name

```html
<!DOCTYPE html>
<html lang="en">
<head>
<meta charset="utf-8">
<title>Pelton Ledger — Flyer</title>
<link rel="stylesheet" href="https://fonts.googleapis.com/css2?family=Roboto+Condensed:wght@400;700&family=Montserrat:wght@400;500&display=swap">
<style>
  :root {
    --canvas: #6b737a;
    --teal: #1ab393;
    --teal-light: #8fd8c6;
    --mint: #e1f4ef;
    --ink: #25302f;
    --night: #2a2d30;
    --white: #ffffff;
    --photo-light: #ddd3c6;
    --photo-mid: #c2a88f;
    --photo-dark: #7d6656;
    --partner-blue: #1eb2e6;
  }
  html, body {
    margin: 0;
    padding: 0;
    width: 1200px;
    height: 2760px;
    overflow: hidden;
    background: var(--canvas);
  }
  .flyer {
    position: absolute;
    left: 50px;
    top: 672px;
    width: 1100px;
    height: 1416px;
    display: block;
  }
  .brand-name {
    font-family: "Montserrat", sans-serif;
    font-weight: 400;
    fill: var(--white);
    letter-spacing: 6px;
  }
  .tagline {
    font-family: "Roboto Condensed", sans-serif;
    font-weight: 700;
    fill: var(--white);
  }
  .section-title {
    font-family: "Roboto Condensed", sans-serif;
    font-weight: 700;
    fill: var(--white);
  }
  .service {
    font-family: "Roboto Condensed", sans-serif;
    font-weight: 700;
    fill: var(--ink);
  }
  .contact {
    font-family: "Roboto Condensed", sans-serif;
    font-weight: 700;
    fill: var(--teal);
  }
  .accreditation {
    font-family: "Roboto Condensed", sans-serif;
    font-weight: 700;
    fill: var(--night);
  }
  .agent-note {
    font-family: "Roboto Condensed", sans-serif;
    font-weight: 700;
    fill: var(--white);
  }
</style>
</head>
<body>
<svg class="flyer" viewBox="0 0 895 1152" preserveAspectRatio="none" xmlns="http://www.w3.org/2000/svg">
  <defs>
    <linearGradient id="photoTone" x1="0" y1="0" x2="1" y2="1">
      <stop offset="0" stop-color="var(--photo-light)"/>
      <stop offset="0.55" stop-color="var(--photo-mid)"/>
      <stop offset="1" stop-color="var(--photo-dark)"/>
    </linearGradient>
  </defs>

  <!-- base -->
  <rect class="flyer-base" width="895" height="1152" fill="var(--mint)"/>

  <!-- hero photo area -->
  <path class="hero-photo" role="img" aria-label="Photo: an accountant shaking hands with a client across a cafe table while a colleague smiles"
        d="M0,0 H895 V500 C650,520 360,470 0,215 Z" fill="url(#photoTone)"/>

  <!-- swooshes under photo -->
  <path class="swoosh-light" d="M0,215 C200,400 450,510 895,500 V520 C430,540 170,420 0,245 Z" fill="var(--teal-light)"/>
  <path class="swoosh-main" d="M60,300 C260,470 520,530 895,490 V570 C560,590 260,510 60,300 Z" fill="var(--teal)"/>

  <!-- top-right brand disc -->
  <circle class="brand-disc" cx="800" cy="-60" r="330" fill="var(--teal)"/>
  <circle class="brand-mark" cx="740" cy="70" r="40" fill="none" stroke="var(--white)" stroke-width="4"/>
  <text class="brand-name" x="740" y="150" font-size="22" text-anchor="middle">PELTON LEDGER</text>

  <!-- tagline ribbon -->
  <path class="tagline-ribbon" d="M560,367 H895 V457 H560 A45,45 0 0 1 560,367 Z" fill="var(--teal)"/>
  <text class="tagline" x="857" y="403" font-size="31" text-anchor="end">TAXATION AND</text>
  <text class="tagline" x="857" y="441" font-size="31" text-anchor="end">BUSINESS ACCOUNTANT</text>

  <!-- services heading -->
  <rect class="section-title-box" x="337" y="627" width="213" height="50" fill="var(--teal)"/>
  <rect class="section-title-rule" x="337" y="680" width="213" height="4" fill="var(--teal)"/>
  <text class="section-title" x="443" y="665" font-size="33" text-anchor="middle">SERVICES</text>

  <!-- services list -->
  <g class="service-ticks" fill="none" stroke="var(--teal)" stroke-width="5" stroke-linecap="round" stroke-linejoin="round">
    <polyline points="58,734 67,744 86,722"/>
    <polyline points="58,791 67,801 86,779"/>
    <polyline points="58,846 67,856 86,834"/>
    <polyline points="488,734 497,744 516,722"/>
    <polyline points="488,791 497,801 516,779"/>
    <polyline points="488,846 497,856 516,834"/>
  </g>
  <text class="service" x="105" y="745" font-size="27">Small Business Taxation</text>
  <text class="service" x="105" y="802" font-size="27">Company &amp; Trust Tax Returns</text>
  <text class="service" x="105" y="857" font-size="27">Rental Property Returns</text>
  <text class="service" x="537" y="745" font-size="27">Capital Gains Tax</text>
  <text class="service" x="537" y="802" font-size="27">Individual Tax Returns</text>
  <text class="service" x="537" y="857" font-size="27">BAS and IAS lodgements</text>

  <!-- footer bands -->
  <path class="footer-band" d="M0,860 C220,950 560,990 895,950 V1152 H0 Z" fill="var(--night)"/>
  <path class="footer-swoosh" d="M170,915 C450,975 720,950 895,860 V975 C640,1010 380,990 170,915 Z" fill="var(--teal)"/>

  <!-- contact details -->
  <g class="icon-phone" transform="translate(61,1006) scale(0.72) translate(-64,-1024)">
    <path d="M66,1028 c4,-4 9,-4 11,0 l5,8 c2,4 0,7 -3,9 c2,6 7,11 13,13 c2,-3 5,-5 9,-3 l8,5 c4,2 4,7 0,11 l-4,4 c-6,5 -20,-1 -31,-12 c-11,-11 -17,-25 -12,-31 Z" fill="var(--teal)"/>
  </g>
  <text class="contact contact-phone" x="104" y="1040" font-size="46">123.456.7809</text>

  <g class="icon-mail">
    <rect x="69" y="1058" width="20" height="14" fill="var(--teal)"/>
    <polyline points="69,1058 79,1066 89,1058" fill="none" stroke="var(--night)" stroke-width="2"/>
  </g>
  <text class="contact contact-email" x="108" y="1074" font-size="24">info@peltonledger.com</text>

  <g class="icon-web" fill="none" stroke="var(--teal)" stroke-width="2">
    <circle cx="79" cy="1101" r="8"/>
    <ellipse cx="79" cy="1101" rx="3.5" ry="8"/>
    <line x1="71" y1="1101" x2="87" y2="1101"/>
  </g>
  <text class="contact contact-web" x="108" y="1110" font-size="24">www.peltonledger.com</text>

  <!-- accreditations -->
  <rect class="accreditation-card" x="467" y="1012" width="165" height="100" fill="var(--white)"/>
  <text class="accreditation" x="512" y="1068" font-size="40" text-anchor="middle">QLA</text>
  <rect class="accreditation-square" x="572" y="1030" width="44" height="44" fill="var(--teal)"/>
  <text class="accreditation" x="549" y="1101" font-size="10.5" text-anchor="middle">Pelton Ledger is a QLA Business</text>

  <circle class="partner-badge" cx="705" cy="1066" r="47" fill="var(--partner-blue)" stroke="var(--white)" stroke-width="4"/>

  <circle class="registration-badge" cx="812" cy="1055" r="34" fill="var(--white)"/>
  <text class="agent-note" x="812" y="1104" font-size="10" text-anchor="middle">Tax agent</text>
  <text class="agent-note" x="812" y="1116" font-size="10" text-anchor="middle">10482213</text>
</svg>
</body>
</html>
```